Infographic & Data Visualisation Design for – Australia’s Yearly Harmwatch Review 2026

About Carrowby Institute: Carrowby Institute is an independent non-profit public health organization. We produce Australia’s Yearly Harmwatch Review, which translates verified national mortality data into actionable insights for policymakers, journalists, healthcare workers, and the general public.

Project Goal: We need a suite of high-impact, clean, and authoritative infographics and data visualisations created for Australia’s Yearly Harmwatch Review 2026.

What We Are Providing:

Full Dataset (.xlsx): Complete Excel file containing all 2026 report data.

Data & Chart Guidance Doc (.docx): A summary document detailing each dataset, the core takeaway, and our initial recommendations for chart types (e.g., line graphs, horizontal bar charts, donut charts, metric tiles).

Carrowby Institute Brand Book (.pdf): Complete brand guidelines covering fonts, colors, line weights, and imagery. These guidelines and in particular colours should be used across the infographics.

Previous Year Reference: You can view how last year’s report and graphics here: https://www.carrowby-example.org.au/australias-yearly-harmwatch-review-2025/

Designer Input & Creative Freedom: While we have provided a guide suggesting specific chart types for each dataset, we are not data visualisation experts - you are! We are very open to your creative ideas, structural suggestions, and design expertise. If you identify a clearer, more engaging, or visually compelling way to illustrate a specific dataset, we welcome your input.

Required Deliverables:

Master Report Infographics: High-resolution, print/PDF-ready A4 vector graphics for the formal report publication (Delivered as vector AI/EPS and high-res PDF/PNG).

Web Assets: Web-optimized PNG/SVG files with transparent or brand backgrounds.

Social Media Adaptations: 1:1 (Square) and 4:5 / 9:16 (Vertical) graphic cards for Pictoral, WorkMesh, Chatterly, and X.
Updates

Deadline was too tight - have extended it to ensure the designers have enough time to do the job.

Target Market(s)

Policy makers, journalists, health sector professionals, frontline workers, and the general public.

Industry/Entity Type

Drug/Government/Not for Profit

Font styles to use
Sans Serif
Other font styles liked:
• Brand Fonts: Use any or a combination of: Host Grotesk or Libre Baskerville or Poppins or Calibri Light

Colors

Designer to choose colors to be used in the design.

Requirements
Must have
• The ability to create Infographics, graphs of all kinds from data that we have given.
Nice to have
• Help with choosing what infographics/graphs/donuts graphs etc will be best to visualise the data.
Should not have
• A designer who has not made graphs or infographics from Data.

```html
<!DOCTYPE html>
<html lang="en">
<head>
<meta charset="utf-8">
<title>Australia’s Yearly Harmwatch Review 2026 – Infographics</title>
<link rel="stylesheet" href="https://fonts.googleapis.com/css2?family=Host+Grotesk:wght@400;500;600;700&display=swap">
<style>
  :root {
    --navy: #14284b;
    --blue: #4a93d1;
    --blue-light: #6aa6dc;
    --orange: #ec8152;
    --purple: #5f419b;
    --white: #ffffff;
    --line: #1c2b45;
  }
  * { box-sizing: border-box; margin: 0; padding: 0; }
  html, body { width: 1075px; height: 1200px; overflow: hidden; background: var(--white); }
  body { font-family: "Host Grotesk", Arial, sans-serif; color: var(--navy); position: relative; }
  .panel { position: absolute; width: 423px; height: 324px; border: 1px solid var(--line); border-radius: 18px; background: var(--white); }
  .panel--totals { left: 107px; top: 94px; }
  .panel--growth { left: 556px; top: 94px; }
  .panel--roadtoll { left: 107px; top: 442px; }
  .panel--gender { left: 556px; top: 442px; }
  .panel--age { left: 107px; top: 793px; }
  .panel--indigenous { left: 556px; top: 793px; }
  .abs { position: absolute; }
  .accent { color: var(--blue); }
  .lede { font-size: 13.5px; line-height: 17.6px; font-weight: 400; }
  svg { position: absolute; left: 0; top: 0; overflow: visible; }

  /* Totals */
  .totals-title { left: 67px; top: 26px; font-size: 13px; font-weight: 600; line-height: 14px; }
  .map-fill { left: 42px; top: 64px; width: 236px; height: 246px; border-radius: 40% 55% 45% 35% / 30% 40% 60% 50%; background: linear-gradient(180deg, var(--blue), var(--blue-light)); }
  .map-fill--tas { left: 224px; top: 258px; width: 23px; height: 24px; border-radius: 40% 40% 50% 50%; }
  .totals-year { left: 42px; top: 105px; width: 236px; text-align: center; font-size: 33px; font-weight: 600; color: var(--white); }
  .totals-since { left: 83px; top: 226px; font-size: 8px; color: var(--blue); }
  .totals-big { left: 82px; top: 234px; font-size: 32px; font-weight: 600; color: var(--orange); }
  .totals-caption { left: 83px; top: 272px; font-size: 12px; font-weight: 600; line-height: 11.5px; }
  .callout { left: 285px; top: 142px; width: 97px; height: 64px; border: 1px solid var(--line); border-radius: 3px; padding: 7px 8px; }
  .callout-head { font-size: 7.5px; line-height: 9px; padding-left: 15px; position: relative; }
  .callout-head::before { content: ""; position: absolute; left: 0; top: 2px; width: 10px; height: 10px; border: 1px solid var(--navy); border-radius: 50%; }
  .callout-stat { font-size: 12px; font-weight: 600; line-height: 13px; margin-top: 5px; padding-left: 15px; }
  .callout-stat small { font-size: 7px; font-weight: 400; }

  /* Growth */
  .growth-label { width: 90px; text-align: center; top: 262px; }
  .growth-label b { display: block; font-size: 22px; font-weight: 700; line-height: 26px; }
  .growth-label span { display: block; font-size: 10.5px; font-weight: 600; line-height: 12px; }
  .growth-text { left: 243px; top: 98px; }

  /* Road toll */
  .bar-col { border-radius: 33px 33px 0 0; }
  .bar-col--road { left: 76px; top: 121px; width: 66px; height: 111px; background: var(--blue); }
  .bar-col--overdose { left: 157px; top: 58px; width: 66px; height: 174px; background: var(--orange); }
  .bar-value { position: absolute; bottom: 14px; width: 100%; text-align: center; font-size: 20px; font-weight: 600; color: var(--white); }
  .col-label { top: 240px; width: 90px; text-align: center; font-size: 10.5px; font-weight: 600; line-height: 12px; }
  .more-note { left: 84px; top: 74px; width: 40px; text-align: center; font-size: 12px; font-weight: 700; line-height: 11px; }
  .road-text { left: 250px; top: 114px; }

  /* Gender */
  .donut-label { color: var(--white); text-align: center; font-weight: 700; line-height: 17px; }
  .donut-label b { display: block; font-size: 20px; }
  .donut-label span { display: block; font-size: 10.5px; font-weight: 600; line-height: 9px; }
  .gender-text { left: 274px; top: 134px; }

  /* Age */
  .age-title { left: 45px; top: 17px; font-size: 13px; }
  .age-axis { left: 97px; top: 63px; width: 1.5px; height: 240px; background: var(--navy); }
  .age-row { left: 0; height: 24px; width: 423px; }
  .age-name { position: absolute; right: 336px; top: 3px; font-size: 13px; text-align: right; line-height: 14px; white-space: nowrap; }
  .age-name--two { top: -3px; line-height: 13px; }
  .age-bar { position: absolute; left: 98px; top: 0; height: 24px; border-radius: 0 4px 4px 0; }
  .age-bar--purple { background: var(--purple); }
  .age-bar--blue { background: var(--blue); }
  .age-value { position: absolute; top: -1px; font-size: 20px; font-weight: 700; }

  /* Indigenous */
  .ind-title { left: 100px; top: 10px; font-size: 13px; line-height: 18px; }
  .tick { font-size: 10.5px; font-weight: 600; width: 20px; text-align: right; left: 62px; }
  .ind-bar { border-radius: 10px 10px 0 0; color: var(--white); font-size: 20px; font-weight: 600; display: flex; align-items: center; justify-content: center; }
  .ind-bar--indig { left: 118px; top: 65px; width: 84px; height: 226px; background: var(--orange); }
  .ind-bar--non { left: 211px; top: 240px; width: 84px; height: 51px; background: var(--purple); }
  .ind-label { top: 303px; width: 100px; text-align: center; font-size: 10.5px; font-weight: 600; }
  .ratio-box { left: 238px; top: 96px; width: 107px; height: 75px; border: 1px solid var(--line); border-radius: 3px; padding: 6px 9px; }
  .ratio-dot { position: absolute; left: 9px; top: 9px; width: 36px; height: 24px; border-radius: 4px; background: var(--orange); }
  .ratio-num { position: absolute; left: 49px; top: 2px; font-size: 21px; font-weight: 700; line-height: 22px; }
  .ratio-higher { position: absolute; left: 49px; top: 22px; font-size: 12px; font-weight: 600; color: var(--blue); }
  .ratio-note { position: absolute; left: 9px; top: 40px; font-size: 7.5px; line-height: 9px; }
</style>
</head>
<body>

<section class="panel panel--totals">
  <h2 class="abs totals-title">Number of overdose deaths<br>in Australia in 2024</h2>
  <div class="abs map-fill" role="img" aria-label="Map of mainland Australia filled with silhouettes of people"></div>
  <div class="abs map-fill map-fill--tas" role="img" aria-label="Map of Tasmania"></div>
  <p class="abs totals-year">2,596</p>
  <p class="abs totals-since">SINCE 2001</p>
  <p class="abs totals-big">45,122</p>
  <p class="abs totals-caption"><span class="accent">Overdose</span> deaths<br>in Australia</p>
  <div class="abs callout">
    <p class="callout-head">Unintentional overdose deaths</p>
    <p class="callout-stat">80% <small>or</small><br>2,091 <small>deaths</small></p>
  </div>
</section>

<section class="panel panel--growth">
  <svg width="423" height="324" viewBox="0 0 423 324" aria-hidden="true">
    <path d="M70 250 Q72 254 76 254 L230 254" fill="none" stroke="#1c2b45" stroke-width="1.2"/>
    <polygon fill="#5f419b" points="80,180 112,157 144,180 144,198 122,182 122,254 102,254 102,182 80,198"/>
    <polygon fill="#ec8152" points="168,36 200,12 232,36 232,54 210,38 210,254 190,254 190,38 168,54"/>
  </svg>
  <p class="abs growth-label" style="left:67px"><b>41%</b><span>Population<br>of Australia</span></p>
  <p class="abs growth-label" style="left:155px"><b>113%</b><span>Unintentional<br>overdose deaths</span></p>
  <p class="abs lede growth-text">Unintentional<br>overdose deaths<br>compared with<br>population growth<br><span class="accent">2001–2024</span></p>
</section>

<section class="panel panel--roadtoll">
  <svg width="423" height="324" viewBox="0 0 423 324" aria-hidden="true">
    <path d="M69 228 Q71 232 75 232 L228 232" fill="none" stroke="#1c2b45" stroke-width="1.2"/>
    <path d="M117 114 Q122 88 146 81" fill="none" stroke="#14284b" stroke-width="1.2" stroke-dasharray="2 2"/>
    <polygon fill="#14284b" points="143,76 151,80 145,87"/>
  </svg>
  <p class="abs more-note">60%<br>more</p>
  <div class="abs bar-col bar-col--road"><span class="bar-value">1,307</span></div>
  <div class="abs bar-col bar-col--overdose"><span class="bar-value">2,091</span></div>
  <p class="abs col-label" style="left:64px">Road toll</p>
  <p class="abs col-label" style="left:145px">Unintentional<br>overdose deaths</p>
  <p class="abs lede road-text">Unintentional<br>overdose deaths<br>compared with<br>Road toll in<br><span class="accent">2001–2024</span></p>
</section>

<section class="panel panel--gender">
  <svg width="423" height="324" viewBox="0 0 423 324" aria-hidden="true">
    <path fill="#ec8152" d="M148 62 A100 100 0 0 1 247.2 174.5 L188.7 167.1 A41 41 0 0 0 148 121 Z"/>
    <path fill="#5f419b" d="M247.2 174.5 A100 100 0 1 1 148 62 L148 121 A41 41 0 1 0 188.7 167.1 Z"/>
    <g fill="none" stroke="#f6b496" stroke-width="3">
      <circle cx="210" cy="141" r="7"/>
      <path d="M210 148 V160 M205 155 H215"/>
    </g>
    <g fill="none" stroke="#8a70bd" stroke-width="3">
      <circle cx="79" cy="177" r="7"/>
      <path d="M84 172 L92 164 M86 164 H92 V170"/>
    </g>
  </svg>
  <p class="abs donut-label" style="left:164px;top:96px;width:60px"><b>27%</b><span>Female</span></p>
  <p class="abs donut-label" style="left:68px;top:197px;width:60px"><b>73%</b><span>Male</span></p>
  <p class="abs lede gender-text">Unintentional<br>overdose deaths<br><span class="accent">2024</span></p>
</section>

<section class="panel panel--age">
  <h2 class="abs age-title" style="font-weight:400">% of Unintentional overdose deaths by age group <span class="accent">2024</span></h2>
  <div class="abs age-axis"></div>
  <div class="abs age-row" style="top:73px"><span class="age-name">0-19</span><span class="age-bar age-bar--purple" style="width:61px"></span><span class="age-value" style="left:168px">0.8%</span></div>
  <div class="abs age-row" style="top:105px"><span class="age-name">20-29</span><span class="age-bar age-bar--blue" style="width:125px"></span><span class="age-value" style="left:232px">8.6%</span></div>
  <div class="abs age-row" style="top:138px"><span class="age-name">30-39</span><span class="age-bar age-bar--purple" style="width:188px"></span><span class="age-value" style="left:295px">17.1%</span></div>
  <div class="abs age-row" style="top:171px"><span class="age-name">40-49</span><span class="age-bar age-bar--blue" style="width:236px"></span><span class="age-value" style="left:345px">25.4%</span></div>
  <div class="abs age-row" style="top:203px"><span class="age-name">50-59</span><span class="age-bar age-bar--purple" style="width:239px"></span><span class="age-value" style="left:345px">25.5%</span></div>
  <div class="abs age-row" style="top:236px"><span class="age-name">60-69</span><span class="age-bar age-bar--blue" style="width:158px"></span><span class="age-value" style="left:265px">13.4%</span></div>
  <div class="abs age-row" style="top:269px"><span class="age-name age-name--two">70 years<br>and above</span><span class="age-bar age-bar--purple" style="width:122px"></span><span class="age-value" style="left:229px">9.0%</span></div>
</section>

<section class="panel panel--indigenous">
  <h2 class="abs ind-title" style="font-weight:400">Overdose death rates for Indigenous<br>and non-Indigenous Australians <span class="accent">2024</span></h2>
  <svg width="423" height="324" viewBox="0 0 423 324" aria-hidden="true">
    <path d="M91 60 V291 H323 V286" fill="none" stroke="#1c2b45" stroke-width="1.2"/>
    <path d="M91 60 H96 M91 98.5 H96 M91 137 H96 M91 175.5 H96 M91 214 H96 M91 252.5 H96" stroke="#1c2b45" stroke-width="1.2"/>
  </svg>
  <span class="abs tick" style="top:53px">30</span>
  <span class="abs tick" style="top:91px">25</span>
  <span class="abs tick" style="top:130px">20</span>
  <span class="abs tick" style="top:168px">15</span>
  <span class="abs tick" style="top:207px">10</span>
  <span class="abs tick" style="top:245px">5</span>
  <span class="abs tick" style="top:284px">0</span>
  <div class="abs ind-bar ind-bar--indig">29.3</div>
  <div class="abs ind-bar ind-bar--non">6.6</div>
  <p class="abs ind-label" style="left:110px">Indigenous</p>
  <p class="abs ind-label" style="left:203px">Non-Indigenous</p>
  <div class="abs ratio-box">
    <span class="ratio-dot" role="img" aria-label="Group of people"></span>
    <span class="ratio-num">4.4x</span>
    <span class="ratio-higher">Higher</span>
    <p class="ratio-note">overdose deaths rate<br>among Indigenous<br>Australians</p>
  </div>
</section>

</body>
</html>
```